Duct Manufacturing Company new to the industry needs business card and stationary design

we are sheet metal duct manufacturers looking for a business card design to fit my new business logo.
nothing to crazy that will date, but want it to stand out from the crowed.
I'm sure you guys will work it out.

Industry/Entity Type

Business

Contact Information for Business Card

Wade Collin
Director

Address
17 Paverly St
Merrindale NSW 2741

0438 657 904

Sales@flowbend.com.au

Font styles to use
Other font styles liked:
• BankGothic md bt

Requirements
Nice to have
• Like the idea of corner rounded to match logo
• like to keep colours flowing
• font I like sharp square not rounded

```html
<!DOCTYPE html>
<html lang="en">
<head>
<meta charset="utf-8">
<title>Flowbend Industries – Business Card</title>
<link rel="stylesheet" href="https://fonts.googleapis.com/css2?family=Michroma&family=Montserrat:wght@400;500&display=swap">
<style>
  :root {
    --backdrop: #a6a6a6;
    --card-black: #151515;
    --card-white: #fbfbfb;
    --brand-blue: #1c6fb8;
    --brand-blue-deep: #1a4590;
    --brand-green: #7dc242;
    --text-light: #ffffff;
    --logo-grey: #8d8f92;
  }
  * { box-sizing: border-box; margin: 0; padding: 0; }
  html, body { width: 1200px; height: 1200px; overflow: hidden; }
  body {
    background: var(--backdrop);
    position: relative;
    font-family: "Montserrat", Arial, sans-serif;
  }
  .card {
    position: absolute;
    width: 714px;
    height: 420px;
    border-radius: 28px;
    overflow: hidden;
  }
  .card-front { left: 238px; top: 117px; background: var(--card-black); }
  .card-back { left: 230px; top: 643px; background: var(--card-white); }

  .wordmark {
    position: absolute;
    text-align: center;
    font-family: "Michroma", Arial, sans-serif;
    font-weight: 400;
    line-height: 1.25;
  }
  .wordmark-front { left: 0; right: 0; top: 245px; color: var(--logo-grey); }
  .wordmark-back { left: 20px; width: 300px; top: 235px; color: var(--logo-grey); }
  .wordmark .name { font-size: 34px; letter-spacing: 1px; display: block; }
  .wordmark .sub { font-size: 22px; letter-spacing: 5px; display: block; }
  .wordmark-back .name { font-size: 27px; }
  .wordmark-back .sub { font-size: 18px; letter-spacing: 4px; }
  .mark-dot {
    position: absolute;
    border-radius: 50%;
    background: var(--brand-blue);
  }
  .mark-dot-front { width: 60px; height: 60px; left: 327px; top: 150px; }
  .mark-dot-back { width: 50px; height: 50px; left: 145px; top: 160px; }

  .card-back svg { position: absolute; inset: 0; }
  .contact {
    position: absolute;
    left: 402px;
    top: 104px;
    color: var(--text-light);
  }
  .contact .person {
    font-family: "Michroma", Arial, sans-serif;
    font-size: 21px;
    letter-spacing: 1.5px;
  }
  .contact .role { font-size: 16px; margin-top: 6px; letter-spacing: 0.5px; }
  .contact ul { list-style: none; margin-top: 22px; }
  .contact li {
    font-size: 19px;
    line-height: 27px;
    display: flex;
    align-items: center;
    gap: 16px;
  }
  .contact li svg { position: static; width: 19px; height: 15px; fill: var(--text-light); }
  .contact .address { font-size: 19px; line-height: 24px; margin-top: 4px; }
</style>
</head>
<body>
  <section class="card card-front">
    <div class="mark-dot mark-dot-front"></div>
    <div class="wordmark wordmark-front">
      <span class="name">FLOWBEND</span>
      <span class="sub">INDUSTRIES</span>
    </div>
  </section>

  <section class="card card-back">
    <svg width="714" height="420" viewBox="0 0 714 420">
      <defs>
        <linearGradient id="panelBlue" x1="0" y1="0" x2="0" y2="1">
          <stop offset="0" stop-color="#1f78c1"/>
          <stop offset="1" stop-color="#1a4590"/>
        </linearGradient>
      </defs>
      <path d="M300 0 C372 120 372 300 298 420 L714 420 L714 0 Z" fill="url(#panelBlue)"/>
      <path d="M268 0 C345 115 356 300 292 420" fill="none" stroke="var(--brand-green)" stroke-width="7"/>
    </svg>
    <div class="mark-dot mark-dot-back"></div>
    <div class="wordmark wordmark-back">
      <span class="name">FLOWBEND</span>
      <span class="sub">INDUSTRIES</span>
    </div>
    <div class="contact">
      <p class="person">WADE COLLIN</p>
      <p class="role">Director</p>
      <ul>
        <li><svg viewBox="0 0 20 16"><path d="M2 5 C2 1 18 1 18 5 L14 6 L13 4 L7 4 L6 6 Z M5 8 L15 8 L17 15 L3 15 Z"/></svg>0438 657 904</li>
        <li><svg viewBox="0 0 16 16"><circle cx="8" cy="8" r="7" fill="none" stroke="#fff" stroke-width="1.5"/><path d="M1 8 H15 M8 1 V15" stroke="#fff" stroke-width="1.3"/></svg>flowbend.com.au</li>
        <li><svg viewBox="0 0 20 14"><path d="M0 0 H20 V14 H0 Z M2 2 L10 8 L18 2" fill="none" stroke="#fff" stroke-width="2"/></svg>Sales@flowbend.com.au</li>
      </ul>
      <p class="address">17 Paverly St<br>Merrindale NSW 2741</p>
    </div>
  </section>
</body>
</html>
```